Webdesign für Steuerberaterin
Zielgruppe
Ich bin Steuerberaterin. Meine Zielgruppe sind sowohl Privatpersonen als auch Unternehmer sowie Männer und Frauen.
Aufgabenstellung
Bitte mein Logo und Foto mit berücksichtigen. Ich möchte keine Website, auf der alle 'Reiter' als eine Seite von oben nach unten durchlaufen. Sondern wirklich einzelne, voneinander getrennte Seiten.

```html
<!DOCTYPE html>
<html lang="de">
<head>
<meta charset="utf-8">
<title>Petra Brandner – Steuerberaterin – Webdesign</title>
<link href="https://fonts.googleapis.com/css2?family=Cabin:ital,wght@0,400;0,500;0,600;1,400&family=Poppins:wght@300;400&display=swap" rel="stylesheet">
<style>
:root{
  --navy:#0b4a6b;
  --ink:#0d4766;
  --teal:#86cdd3;
  --teal-soft:#a9dde0;
  --black:#1b1b1b;
  --grey:#6f7a80;
  --paper:#ffffff;
  --stage:#ffffff;
}
*{box-sizing:border-box;margin:0;padding:0}
html,body{width:1200px;height:800px;overflow:hidden;background:var(--stage)}
body{position:relative;font-family:"Cabin",sans-serif;color:var(--ink)}
.page{position:absolute;width:366px;background:var(--paper);box-shadow:0 4px 6px rgba(0,0,0,.35);overflow:hidden}
.topbar{height:18px;background:var(--navy);color:#fff;font-style:italic;font-size:4.6px;display:flex;align-items:center;padding-left:21px}
.topbar span{white-space:nowrap}
.topbar .addr{width:91px}
.topbar .tel{width:56px}
.topbar .mail{width:94px}
.brand{position:absolute;left:37px;top:30px;display:flex;align-items:center;gap:3px;font-size:6.5px;font-weight:600;color:var(--ink)}
.brand i{display:block;width:6px;height:6px;border-radius:50%;background:var(--ink)}
.nav{position:absolute;top:32px;right:37px;display:flex;gap:10px;font-size:5.2px;font-weight:500;color:var(--black)}
.nav .active{color:var(--teal)}
.h1{position:absolute;left:37px;font-size:9px;font-weight:600;color:var(--teal);letter-spacing:.1px}
.footer{position:absolute;left:0;width:366px;height:54px;background:var(--navy);color:#fff;font-size:4.4px;font-style:italic;line-height:7px}
.footer .c1{position:absolute;left:37px;top:9px}
.footer .c1 b{font-style:normal;font-weight:600}
.footer .c2{position:absolute;left:136px;top:16px}
.footer .c3{position:absolute;left:264px;top:20px}
.footer .c3 .copy{margin-top:6px}
p,li{font-size:5.6px;line-height:7.2px}

.service{position:absolute;color:var(--ink)}
.service svg{display:block;margin-bottom:3px}
.service .title{font-size:6.2px;line-height:9.5px;font-weight:500}
.service p{margin-top:4px}
.service .sub{font-size:6.2px;line-height:9.5px;font-weight:500;margin-top:4px}

.hero{position:absolute;left:0;top:55px;width:366px;height:67px;background:linear-gradient(100deg,#4b4d4f 0%,#8a8d8f 30%,#c9cdcf 55%,#d9dcdd 100%)}
.hero-text{position:absolute;left:160px;top:72px;width:184px;height:43px;border-radius:18px;background:rgba(169,221,224,.45)}
.hero-head{position:absolute;left:169px;top:75px;color:#fff;font-weight:600;font-size:11px;line-height:12px}
.hero-sub{position:absolute;left:169px;top:89px;color:#fff;font-weight:600;font-size:9.5px;line-height:10.5px}
.intro{position:absolute;left:87px;top:147px;width:196px}
.intro .h2{font-size:7px;font-weight:600;color:var(--teal);margin-bottom:8px}
.intro p{color:var(--black);margin-bottom:7.5px;font-size:5.9px;line-height:7.7px}

.contact-addr{position:absolute;left:37px;top:93px;font-family:"Poppins",sans-serif;font-size:6.7px;line-height:9.3px;color:var(--black)}
.contact-tel{position:absolute;left:37px;top:140px;font-family:"Poppins",sans-serif;font-weight:300;font-size:5.9px;line-height:8.9px;color:var(--grey)}
.contact-note{position:absolute;left:37px;top:176px;width:112px;font-family:"Poppins",sans-serif;font-size:6.8px;line-height:9.1px;color:var(--ink)}
.contact-note .lead{margin-bottom:4px}
.form{position:absolute;left:183px;top:117px;width:143px;height:135px;border:1px solid #9bb3c2;background:#fff;font-size:4.8px;color:var(--ink)}
.form .label{position:absolute;left:6px}
.form .line{position:absolute;left:38px;width:95px;border-top:.6px solid #7d9fb1}
.form .send{position:absolute;right:9px;bottom:17px;width:34px;height:12px;border-radius:6px;background:var(--teal-soft);color:#fff;font-size:4.6px;display:flex;align-items:center;justify-content:center}

.portrait{position:absolute;left:37px;top:97px;width:244px;height:163px;background:linear-gradient(90deg,#dcdcdc 0%,#ececec 45%,#e4e4e4 70%,#cfd2d4 100%)}
.bubble{position:absolute;left:222px;top:105px;width:93px;height:148px;border-radius:8px;background:var(--navy);color:#fff;font-family:"Poppins",sans-serif;font-weight:300;font-size:5.6px;line-height:8.6px;padding:8px 5px 0 10px}
.career{position:absolute;left:37px;top:274px}
.career .h2{font-size:9px;font-weight:600;color:var(--teal);margin-bottom:3px}
.career li{list-style:none;font-family:"Poppins",sans-serif;font-weight:300;font-size:5.9px;line-height:8.9px;color:var(--grey)}
</style>
</head>
<body>

<section class="page" style="left:30px;top:97px;height:464px">
  <div class="topbar"><span class="addr">Lindenweg 14, 24589 Seedorf</span><span class="tel">Tel.: 04392 – 7 31 18 40</span><span class="mail">Email: info@brandner-steuer.de</span><span>TERMINE NACH VEREINBARUNG</span></div>
  <div class="brand"><i></i>Petra Brandner</div>
  <nav class="nav"><span>HOME</span><span class="active">LEISTUNGEN</span><span>ÜBER MICH</span><span>KONTAKT</span></nav>
  <h1 class="h1" style="top:80px">MEINE LEISTUNGEN</h1>

  <div class="service" style="left:37px;top:118px;width:90px">
    <svg width="26" height="22" viewBox="0 0 26 22" style="margin-left:25px" fill="none" stroke="#2aa7c9" stroke-width="1"><rect x="1" y="3" width="18" height="15"/><line x1="1" y1="7" x2="19" y2="7"/><line x1="5" y1="1" x2="5" y2="5"/><line x1="15" y1="1" x2="15" y2="5"/><line x1="4" y1="11" x2="13" y2="11"/><line x1="4" y1="14" x2="10" y2="14"/><circle cx="19" cy="16" r="4.5" fill="#fff"/><path d="M19 13.5v2.7h2"/></svg>
    <div class="title">Einkommensteuererklärung<br>Betriebliche Steuererklärungen</div>
    <p style="margin-top:8px;font-size:5.3px;line-height:9px">z.B. Umsatzsteuererklärung,<br>Gewerbesteuererklärung, etc.</p>
  </div>

  <div class="service" style="left:143px;top:116px;width:106px">
    <svg width="18" height="24" viewBox="0 0 18 24" style="margin-left:17px" fill="none" stroke="#2aa7c9" stroke-width="1"><rect x="1" y="1" width="16" height="22" rx="1"/><rect x="3.5" y="3.5" width="11" height="4"/><g fill="#2aa7c9" stroke="none"><rect x="3.5" y="10" width="2.5" height="2"/><rect x="7.5" y="10" width="2.5" height="2"/><rect x="11.5" y="10" width="2.5" height="2"/><rect x="3.5" y="14" width="2.5" height="2"/><rect x="7.5" y="14" width="2.5" height="2"/><rect x="11.5" y="14" width="2.5" height="2"/><rect x="3.5" y="18" width="2.5" height="2"/><rect x="7.5" y="18" width="2.5" height="2"/><rect x="11.5" y="18" width="2.5" height="2"/></g></svg>
    <div class="title">Finanzbuchführung</div>
    <p>Kontierung und Erfassung der Geschäftsvorfälle, ggf. Erfassung Ihrer gesamten Eingangs- und Ausgangsrechnungen sowie Übersicht der offenen Posten, laufende Abstimmung der Konten, regelmäßige Auswertung (BWA, SuSa, etc.)</p>
    <div class="sub">Jahresabschluss (Bilanz)<br>Einnahmenüberschussrechnung</div>
    <div class="sub" style="line-height:8px">Lohnbuchführung</div>
    <p style="margin-top:0">mithilfe der KontoPlan als kompetentem Partner ist auch Ihre Lohnabrechnung bei mir in den besten Händen.</p>
    <p style="margin-top:9px;width:92px">Ich erledige Ihre Buchführung nach den Grundsätzen ordnungsgemäßer Buchführung. Dies sowohl digital, als auch auf Basis von Papierbelegen, die Sie bei mir einreichen („Pendelordner“), je nachdem, wie Sie es sich wünschen. Sie möchten in die Digitalisierung einsteigen, haben es aber bisher nicht geschafft? Dann lassen Sie uns diesen Weg gemeinsam gehen! Falls Sie selbst buchen (wollen), unterstütze ich Sie hierbei natürlich auch gerne.</p>
  </div>

  <div class="service" style="left:258px;top:119px;width:76px">
    <svg width="22" height="22" viewBox="0 0 22 22" style="margin-left:16px" fill="none" stroke="#2aa7c9" stroke-width="1"><circle cx="9" cy="4" r="2.2"/><circle cx="14.5" cy="4" r="2.2"/><circle cx="11.8" cy="9" r="2.2"/><path d="M1 16h5l3 2h6l5-4M1 21h8l7-3"/></svg>
    <div class="title">laufende steuerliche<br>Beratung</div>
    <p style="margin-top:5px">Um ein „böses Erwachen“ durch hohe Nachzahlungen am Ende eines Steuerjahres zu verhindern, behalte ich Ihr laufendes Betriebsergebnis im Blick und kalkuliere anhand Ihrer Zahlen das voraussichtliche Jahresergebnis. So kann ich bereits unterjährig abschätzen wie hoch Ihre zu zahlende Steuer für das Kalenderjahr in etwa ausfallen wird und ggf. Ihre Steuer-Vorauszahlungen nach Absprache mit Ihnen rechtzeitig anpassen lassen.</p>
  </div>

  <footer class="footer" style="top:410px">
    <div class="c1"><b>KONTAKT</b><br>Petra Brandner<br>Steuerberaterin<br>Lindenweg 14<br>24589 Seedorf</div>
    <div class="c2">Tel.: 04392 – 7 31 18 40<br>Fax: 04392 – 7 31 18 XX<br>Email: info@brandner-steuer.de<br>TERMINE NACH VEREINBARUNG</div>
    <div class="c3">Impressum<br>Datenschutz<div class="copy">© Petra Brandner 2021</div></div>
  </footer>
</section>

<section class="page" style="left:420px;top:37px;height:343px">
  <div class="topbar"><span class="addr">Lindenweg 14, 24589 Seedorf</span><span class="tel">Tel.: 04392 – 7 31 18 40</span><span class="mail">Email: info@brandner-steuer.de</span><span>TERMINE NACH VEREINBARUNG</span></div>
  <div class="brand"><i></i>Petra Brandner</div>
  <nav class="nav"><span class="active">HOME</span><span>LEISTUNGEN</span><span>ÜBER MICH</span><span>KONTAKT</span></nav>
  <div class="hero" role="img" aria-label="Foto: Taschenrechner, Stift und Steuerunterlagen auf dem Schreibtisch"></div>
  <div class="hero-text"></div>
  <div class="hero-head">SCHÖN, DASS SIE DA SIND!</div>
  <div class="hero-sub">Ich freue mich, dass Sie den Weg<br>zu mir gefunden haben!</div>
  <div class="intro">
    <div class="h2">SIE SIND BEI MIR GENAU RICHTIG</div>
    <p>Egal, ob Sie Privatperson sind, die Ihre Einkommensteuer-Erklärung in vertrauensvolle Hände geben möchte, oder Unternehmer, der sich z.B. das „Rundum-Sorglos-Paket“ mit Buchführung, Jahresabschluss und Steuererklärungen wünscht.</p>
    <p>Schauen Sie sich hier gerne um und melden Sie sich bei mir –<br>ich bin bei jedem steuerlichen Thema gerne Ihr kompetenter und zuverlässiger Ansprechpartner.</p>
    <p>Für mich ist es eine Selbstverständlichkeit, dass ich auch nach mehr als 12 Jahren Berufserfahrung durch permanente Fortbildungen immer auf dem aktuellsten Stand der relevanten Gesetze und Verordnungen bin. Nur so kann ich Sie bestmöglich beraten.</p>
  </div>
  <footer class="footer" style="top:289px">
    <div class="c1"><b>KONTAKT</b><br>Petra Brandner<br>Steuerberaterin<br>Lindenweg 14<br>24589 Seedorf</div>
    <div class="c2">Tel.: 04392 – 7 31 18 40<br>Fax: 04392 – 7 31 18 XX<br>Email: info@brandner-steuer.de<br>TERMINE NACH VEREINBARUNG</div>
    <div class="c3">Impressum<br>Datenschutz<div class="copy">© Petra Brandner 2021</div></div>
  </footer>
</section>

<section class="page" style="left:420px;top:402px;height:356px">
  <div class="topbar"><span class="addr">Lindenweg 14, 24589 Seedorf</span><span class="tel">Tel.: 04392 – 7 31 18 40</span><span class="mail">Email: info@brandner-steuer.de</span><span>TERMINE NACH VEREINBARUNG</span></div>
  <div class="brand"><i></i>Petra Brandner</div>
  <nav class="nav"><span>HOME</span><span>LEISTUNGEN</span><span>ÜBER MICH</span><span class="active">KONTAKT</span></nav>
  <h1 class="h1" style="top:69px">KONTAKT</h1>
  <div class="contact-addr">Petra Brandner<br>Steuerberaterin<br>Lindenweg 14<br>24589 Seedorf</div>
  <div class="contact-tel">Tel.: 04392 – 7 31 18 40<br>Fax: 04392 – 7 31 18 XX<br>Email: info@brandner-steuer.de</div>
  <div class="contact-note"><div class="lead">Termine nach Vereinbarung</div>Für persönliche Gespräche komme ich gerne zu Ihnen, wir treffen uns per Videokonferenz online oder bei mir im Büro, je nachdem, wie es für Sie am angenehmsten ist.</div>
  <div class="form">
    <span class="label" style="top:10px;font-size:5px">Kontaktformular</span>
    <span class="label" style="top:40px">Name</span><span class="line" style="top:43px"></span>
    <span class="label" style="top:58px">Email</span><span class="line" style="top:62px"></span>
    <span class="label" style="top:85px">Nachricht</span><span class="line" style="top:88px"></span>
    <span class="send">senden</span>
  </div>
  <footer class="footer" style="top:302px">
    <div class="c1"><b>KONTAKT</b><br>Petra Brandner<br>Steuerberaterin<br>Lindenweg 14<br>24589 Seedorf</div>
    <div class="c2">Tel.: 04392 – 7 31 18 40<br>Fax: 04392 – 7 31 18 XX<br>Email: info@brandner-steuer.de<br>TERMINE NACH VEREINBARUNG</div>
    <div class="c3">Impressum<br>Datenschutz<div class="copy">© Petra Brandner 2021</div></div>
  </footer>
</section>

<section class="page" style="left:810px;top:120px;height:418px">
  <div class="topbar"><span class="addr">Lindenweg 14, 24589 Seedorf</span><span class="tel">Tel.: 04392 – 7 31 18 40</span><span class="mail">Email: info@brandner-steuer.de</span><span>TERMINE NACH VEREINBARUNG</span></div>
  <div class="brand"><i></i>Petra Brandner</div>
  <nav class="nav"><span>HOME</span><span>LEISTUNGEN</span><span class="active">ÜBER MICH</span><span>KONTAKT</span></nav>
  <h1 class="h1" style="top:74px">ÜBER MICH</h1>
  <div class="portrait" role="img" aria-label="Porträtfoto der Steuerberaterin vor heller Steinwand"></div>
  <div class="bubble">Ich bin Petra Brandner, Steuerberaterin aus Leidenschaft, und wohne mit meinem Mann und meinem Sohn in Seedorf. Ich habe meinen Beruf „von der Pike auf“ gelernt und möchte Sie gerne kompetent und zuverlässig in Ihrem beruflichen Alltag begleiten und Ihnen „den Rücken freihalten“, so dass Sie sich voll und ganz auf Ihr Kerngeschäft konzentrieren können.</div>
  <div class="career">
    <div class="h2">WERDEGANG</div>
    <ul><li>2004: Abitur</li><li>seit 2008:</li><li>Steuerfachangestellte</li><li>seit 2012: Steuerfachwirtin</li><li>seit 2018: Steuerberaterin</li></ul>
  </div>
  <footer class="footer" style="top:365px">
    <div class="c1"><b>KONTAKT</b><br>Petra Brandner<br>Steuerberaterin<br>Lindenweg 14<br>24589 Seedorf</div>
    <div class="c2">Tel.: 04392 – 7 31 18 40<br>Fax: 04392 – 7 31 18 XX<br>Email: info@brandner-steuer.de<br>TERMINE NACH VEREINBARUNG</div>
    <div class="c3">Impressum<br>Datenschutz<div class="copy">© Petra Brandner 2021</div></div>
  </footer>
</section>

</body>
</html>
```